Northwind Crate Traders Needs a FRESH website

We would like a creative minded designer to take on the task to Re-design our website. Its a simple 5-7 pages. With no cart, no complex html. Just plain information about our company and products we import and export. Pictures added to the product section. Since Our logo its Blue, we would like the designer to use complementing colors in order to make the website look cleaner and modern.

Target Market(s)

The target audience will be companies looking to purchase plastic related products. Companies looking to purchase large quantities of plastic containers (Shampoo bottles, caps, sprayers, mist sprayers, cosmetic containers etc).

Industry/Entity Type

It Company

Font styles to use
Sans Serif

Requirements
Must have
• We have a section in which we would like to add pictures of some of the products we carry, therefore having an easy and clean way to navigate through the pictures will be a plus.

```html
<!DOCTYPE html>
<html lang="en">
<head>
<meta charset="utf-8">
<title>Northwind Crate Traders</title>
<link rel="stylesheet" href="https://fonts.googleapis.com/css2?family=Open+Sans:wght@400;600&display=swap">
<style>
:root{
  --brand:#0a74c8;
  --brand-dark:#0062b0;
  --text:#555;
  --text-dark:#333;
  --nav:#666;
  --panel:#f2f2f2;
  --footer:#eeeeee;
  --bar:#2b2b2b;
  --line:#d5d5d5;
  --hero-a:#2a5e1a;
  --hero-b:#4f8a35;
  --sky-a:#1c57b4;
  --sky-b:#0d3680;
}
*{box-sizing:border-box;margin:0;padding:0}
html,body{width:1150px;height:1200px;overflow:hidden;background:#fff;font-family:"Open Sans",Arial,sans-serif;color:var(--text)}
.page{position:relative;width:1150px;height:1200px}
.abs{position:absolute}
.logo{left:95px;top:0;width:180px;height:127px;background:var(--brand);display:flex;flex-direction:column;align-items:center;justify-content:center;gap:8px;color:#fff;font-size:19px;font-weight:600;text-align:center;line-height:1.15}
.logo-dot{width:36px;height:36px;border-radius:50%;background:#fff}
.search{left:885px;top:29px;width:170px;height:31px;border:1px solid var(--line);border-radius:2px;font-size:13px;color:#999;padding:6px 12px}
.search svg{position:absolute;right:6px;top:5px}
.search::after{content:"";position:absolute;right:30px;top:6px;width:1px;height:18px;background:var(--line)}
.nav{left:473px;top:94px;width:582px;height:33px;border-bottom:2px solid #e3e3e3;display:flex;justify-content:space-between;font-size:14px;color:var(--nav)}
.nav a{text-decoration:none;color:inherit;padding:0 5px;height:33px;position:relative}
.nav a.active{color:var(--brand)}
.nav a.active::after{content:"";position:absolute;left:0;right:0;bottom:-2px;height:4px;background:var(--brand)}
.hero{left:95px;top:140px;width:960px;height:417px;background:linear-gradient(90deg,var(--hero-a) 0%,var(--hero-b) 100%)}
.hero-text{left:35px;top:62px;color:#fff;font-size:19.5px;line-height:30px;text-transform:uppercase}
.dots{left:22px;top:383px;display:flex;gap:10px}
.dots span{width:13px;height:13px;border-radius:50%;background:#bbb}
.dots span:first-child{background:#444;border:2px solid #ccc}
h2{font-weight:600;color:var(--brand)}
.welcome-title{left:98px;top:583px;font-size:27px;line-height:32px}
.welcome-title small{display:block;font-size:21px;line-height:24px}
.welcome-copy{left:98px;top:654px;width:310px;font-size:13px;line-height:22px}
.welcome-img{left:98px;top:791px;width:304px;height:142px;background:linear-gradient(180deg,var(--sky-a),var(--sky-b))}
.products-title{left:427px;top:587px;font-size:20px}
.products-box{left:427px;top:621px;width:304px;height:312px;background:linear-gradient(180deg,#c9dff3 0%,#eaf3fb 40%,#f1f7fd 100%)}
.products-list{left:442px;top:725px;list-style:none;font-size:15px;color:var(--brand);line-height:28px}
.products-list li::before{content:"•";font-size:11px;margin-right:8px;vertical-align:1px}
.news-title{left:751px;top:585px;font-size:20px}
.news{left:753px;top:619px;width:300px;height:314px;background:var(--panel)}
.item{position:absolute;left:10px}
.thumb{width:87px;height:67px;border:3px solid #fff;box-shadow:0 0 3px #bbb}
.t1{background:linear-gradient(180deg,#5aa8d8,#e6d4ae)}
.t2{background:linear-gradient(135deg,#3b8fe0,#8fc5f3)}
.t3{background:linear-gradient(180deg,#86a84a,#eef3e6)}
.item p{position:absolute;left:100px;top:-2px;width:178px;font-size:12px;line-height:16px;color:var(--text-dark);text-align:justify}
.item time{position:absolute;left:100px;top:36px;font-size:13px;color:#888;white-space:nowrap}
.footer{left:0;top:970px;width:1150px;height:172px;background:var(--footer)}
.footer h3{position:absolute;font-weight:400;font-size:16px;color:var(--brand)}
.links{position:absolute;list-style:none;font-size:13px;line-height:24px;color:var(--text-dark)}
.news-copy{left:581px;top:50px;width:240px;font-size:13px;line-height:18px;color:#777}
.email{left:581px;top:103px;width:234px;height:35px;background:#fff;border:1px solid #ddd;border-radius:3px;font-size:12px;color:#444;padding:9px 13px}
.email b{position:absolute;right:1px;top:1px;height:31px;width:62px;background:var(--brand-dark);color:#fff;font-weight:400;font-size:12px;border-radius:3px;text-align:center;line-height:31px}
.social{left:889px;top:57px;display:flex;gap:8px}
.social span{width:31px;height:31px;border-radius:50%}
.bar{left:0;top:1142px;width:1150px;height:58px;background:var(--bar);color:#999;font-size:12px;text-align:center;line-height:62px;word-spacing:2px}
</style>
</head>
<body>
<div class="page">
  <div class="abs logo"><span class="logo-dot"></span>Northwind Crate<br>Traders</div>
  <div class="abs search">Search
    <svg width="20" height="20" viewBox="0 0 20 20"><circle cx="8" cy="8" r="6" fill="none" stroke="#999" stroke-width="2.4"/><line x1="12.5" y1="12.5" x2="18" y2="18" stroke="#999" stroke-width="3"/></svg>
  </div>
  <nav class="abs nav">
    <a class="active">HOME</a><a>ABOUT US</a><a>PRODUCTS</a><a>MISSION STATEMENT</a><a>CONTACT US</a>
  </nav>

  <section class="abs hero" role="img" aria-label="Young woman drinking water from a plastic bottle against a green park background">
    <p class="abs hero-text">A trustworthy company<br>sourcing and importing your needs<br>to your business doorsteps.</p>
    <div class="abs dots"><span></span><span></span><span></span><span></span></div>
  </section>

  <h2 class="abs welcome-title">Welcome to<small>Northwind Crate Traders</small></h2>
  <p class="abs welcome-copy">Northwind Crate Traders will be your first and last stop for sourcing products from all over the world, specifically Asia and South America. We have partners all around the globe that helps us make the best decision in sourcing a product from and to any market.</p>
  <div class="abs welcome-img" role="img" aria-label="Silhouette of a person drinking from a bottle against a bright sun and blue sky"></div>

  <h2 class="abs products-title">Our Products</h2>
  <div class="abs products-box" role="img" aria-label="Water pouring from a clear plastic bottle on a pale blue background"></div>
  <ul class="abs products-list">
    <li>PET</li><li>PET Resin</li><li>PET Containers / bottles</li><li>P.E. P.P. Containers / bottles</li><li>Sprayers / Atomizers / Pumps</li><li>Molds</li><li>Machinery</li>
  </ul>

  <h2 class="abs news-title">Latest News</h2>
  <div class="abs news">
    <div class="item" style="top:19px"><div class="thumb t1" role="img" aria-label="Plastic bottle on a sandy beach"></div><p>Vivamus lobortis sagittis lacus, luctus viverra nunc dignissim</p><time>Apr-8-2014</time></div>
    <div class="item" style="top:119px"><div class="thumb t2" role="img" aria-label="Hand holding a water bottle against blue sky"></div><p>Vivamus lobortis sagittis lacus, luctus viverra nunc dignissim</p><time>Apr-8-2014</time></div>
    <div class="item" style="top:229px"><div class="thumb t3" role="img" aria-label="Row of plastic bottles on grass"></div><p>Vivamus lobortis sagittis lacus, luctus viverra nunc dignissim</p><time>Apr-8-2014</time></div>
  </div>

  <footer class="abs footer">
    <h3 style="left:112px;top:21px">Quick Links</h3>
    <ul class="links" style="left:114px;top:50px"><li>Home</li><li>About us</li><li>Products</li><li>Mission Statement</li></ul>
    <ul class="links" style="left:238px;top:50px"><li>Contact us</li></ul>
    <h3 style="left:345px;top:21px">Support Links</h3>
    <ul class="links" style="left:348px;top:50px"><li>Press</li><li>Legal Notice</li><li>Privacy Policy</li><li>Term of Use</li></ul>
    <ul class="links" style="left:458px;top:50px"><li>Help</li></ul>
    <h3 style="left:579px;top:21px">Newsletters Sign Up</h3>
    <p class="abs news-copy">Sign up for our daily email by entering your information below</p>
    <div class="abs email">Email address<b>SUBMIT</b></div>
    <h3 style="left:890px;top:21px">Connect With Us</h3>
    <div class="abs social" aria-label="Social links">
      <span style="background:#1f5fa8"></span><span style="background:#3aa3dc"></span><span style="background:#e0502e"></span><span style="background:#c9231f"></span>
    </div>
  </footer>
  <div class="abs bar">Copyright © 2014 Northwind Crate Traders. All rights reserved.</div>
</div>
</body>
</html>
```